Lantern Business Cards

Need business cards for my employees at my restaurant.

Needs to include:
Our Logo
Lantern Forks & Cellar
Name: Miriam Toddwell
Title : Owner
Address: 847 Pickering Ave. Pinecrest Harbor, OR 86519
Web: www.lanternkitchenbay.com
Phone: 555-555-0147
Cell: 555-555-0183
Email: info@lanternkitchenbay.com

```html
<!DOCTYPE html>
<html lang="en">
<head>
<meta charset="utf-8">
<title>Lantern Forks &amp; Cellar — Business Cards</title>
<link href="https://fonts.googleapis.com/css2?family=Open+Sans:wght@400;700&display=swap" rel="stylesheet">
<style>
  :root {
    --backdrop: #dcdcdc;
    --card-white: #ffffff;
    --brand-red: #be1e2d;
    --ink-dark: #222222;
    --ink-text: #3a3a3a;
  }
  * { box-sizing: border-box; margin: 0; padding: 0; }
  html, body { width: 1125px; height: 1200px; overflow: hidden; }
  body {
    background: var(--backdrop);
    font-family: "Open Sans", Arial, sans-serif;
    position: relative;
  }
  .card {
    position: absolute;
    left: 150px;
    width: 825px;
    height: 472px;
    border-radius: 26px;
    overflow: hidden;
  }
  .card-front { top: 98px; background: var(--card-white); }
  .card-back { top: 632px; background: var(--brand-red); }

  /* Front */
  .brand-name {
    position: absolute;
    left: 36px; top: 62px;
    width: 290px;
    color: var(--brand-red);
    font-weight: 700;
    font-size: 28px;
    line-height: 1.15;
    text-transform: uppercase;
  }
  .contact-block { position: absolute; left: 36px; top: 162px; }
  .person-name {
    color: var(--brand-red);
    font-weight: 700;
    font-size: 26px;
    line-height: 1.2;
    text-transform: uppercase;
  }
  .person-title { color: var(--ink-text); font-size: 20px; line-height: 1.2; }
  .rule { width: 28px; height: 3px; background: var(--brand-red); margin: 12px 0; }
  .address { color: var(--ink-text); font-size: 20px; line-height: 28px; }
  .contact-list { list-style: none; }
  .contact-list li {
    display: flex; align-items: center; gap: 6px;
    color: var(--ink-text); font-size: 20px; line-height: 27px;
  }
  .contact-list svg { width: 15px; height: 15px; fill: var(--brand-red); flex: none; }

  .accent-band {
    position: absolute;
    right: 0; top: 0;
    width: 220px; height: 100%;
    background: var(--brand-red);
  }
  .accent-mark {
    position: absolute;
    left: 370px; top: 28px;
    width: 416px; height: 416px;
    border-radius: 50%;
    background: var(--ink-dark);
    border: 8px solid var(--card-white);
  }

  /* Back */
  .back-mark {
    position: absolute;
    left: 50%; top: 86px;
    width: 160px; height: 160px;
    margin-left: -80px;
    border-radius: 50%;
    background: var(--card-white);
  }
  .back-name {
    position: absolute;
    left: 0; right: 0; top: 272px;
    text-align: center;
    color: var(--card-white);
    font-weight: 700;
    font-size: 50px;
    line-height: 1.1;
    text-transform: uppercase;
  }
</style>
</head>
<body>

<section class="card card-front">
  <div class="brand-name">Lantern Forks &amp; Cellar</div>

  <div class="contact-block">
    <h1 class="person-name">Miriam Toddwell</h1>
    <p class="person-title">Owner</p>
    <div class="rule"></div>
    <p class="address">847 Pickering Ave.<br>Pinecrest Harbor, OR 86519</p>
    <div class="rule"></div>
    <ul class="contact-list">
      <li><svg viewBox="0 0 16 16"><path d="M3 2h3l1.5 3.5-2 1.2a8 8 0 0 0 3.8 3.8l1.2-2L14 10v3a1 1 0 0 1-1 1A11 11 0 0 1 2 3a1 1 0 0 1 1-1z"/></svg>555-555-0147</li>
      <li><svg viewBox="0 0 16 16"><path d="M4.5 1h7a1 1 0 0 1 1 1v12a1 1 0 0 1-1 1h-7a1 1 0 0 1-1-1V2a1 1 0 0 1 1-1zm.5 2v9h6V3z"/></svg>555-555-0183</li>
      <li><svg viewBox="0 0 16 16"><path d="M1 4h14v9H1zm1.5 1.2v.3L8 9l5.5-3.5v-.3z"/></svg>info@lanternkitchenbay.com</li>
      <li><svg viewBox="0 0 16 16"><circle cx="8" cy="8" r="7"/></svg>www.lanternkitchenbay.com</li>
    </ul>
  </div>

  <div class="accent-band"></div>
  <div class="accent-mark"></div>
</section>

<section class="card card-back">
  <div class="back-mark"></div>
  <div class="back-name">Lantern Forks &amp; Cellar</div>
</section>

</body>
</html>
```